Investment Company Business Card Design

We need a Business Card design for a new company based in Boston called "Olt Investment". We are cooperating with local real estate and construction companies. Our company is very actively and aggressively acquiring primarily residential investment properties either to buy and hold long term or for purposes or renovating and repositioning for re-sale in the market. In addition, we undertake some development projects and acquisitions as opportunities present themselves. the final design should contains information about “Olt" the river boat. we are tenacious, indomitable, and the business have a favorable wind throughout the voyage for all our investment.
sample Info. on Design:
Tem Hollis
CEO
508-xxx-xxxx
415 Marrow St. Suite 108, Boston, MA 02127
Please provide a template also, that we can edit the info later.
Reason: i just got new LOGO Design attached will be use in Business Card Design.
Construction

```html
<!DOCTYPE html>
<html lang="en">
<head>
<meta charset="utf-8">
<title>Olt Investment – Business Card</title>
<link rel="stylesheet" href="https://fonts.googleapis.com/css2?family=Open+Sans:wght@300;400;600&display=swap">
<style>
  :root {
    --backdrop: #e6e4e1;
    --card-black: #231f20;
    --card-white: #ffffff;
    --gold: #c9a44a;
    --gold-light: #e6c978;
    --ink: #3a3a3a;
    --ink-soft: #6b6b6b;
    --paper-text: #d9d9d9;
  }
  * { box-sizing: border-box; margin: 0; padding: 0; }
  html, body {
    width: 1200px; height: 873px; overflow: hidden;
    background: var(--backdrop);
    font-family: "Open Sans", Arial, sans-serif;
  }
  .canvas {
    position: relative; width: 1200px; height: 873px;
    display: flex; align-items: center; justify-content: center; gap: 60px;
  }
  .card {
    position: relative; width: 520px; height: 300px;
    box-shadow: 0 10px 28px rgba(0,0,0,.18);
    overflow: hidden;
  }

  /* Front */
  .card--front { background: var(--card-white); display: flex; }
  .front__band {
    position: relative; width: 200px; height: 100%;
    background: var(--card-black);
    border-right: 4px solid var(--gold);
    padding: 30px 22px;
  }
  .address {
    display: flex; gap: 8px;
    color: var(--paper-text); font-weight: 300; font-size: 11.5px; line-height: 1.6;
  }
  .address svg { flex: none; margin-top: 3px; }
  .brand {
    display: flex; align-items: center; gap: 8px;
    color: var(--gold); font-weight: 600; font-size: 16px; letter-spacing: .5px;
  }
  .front__band .brand { position: absolute; left: 22px; bottom: 34px; }
  .brand__dot { width: 12px; height: 12px; border-radius: 50%; background: var(--gold); flex: none; }

  .front__details {
    flex: 1; display: flex; flex-direction: column; justify-content: flex-end;
    padding: 0 0 44px 110px; gap: 12px;
  }
  .contact-row {
    display: flex; align-items: center; gap: 10px;
    color: var(--ink); font-size: 12px; font-weight: 400;
  }
  .contact-row--name { font-weight: 600; letter-spacing: .6px; margin-bottom: 4px; }
  .tag {
    display: inline-flex; align-items: center; justify-content: center;
    width: 26px; height: 16px; background: var(--gold); color: #fff;
    font-size: 8.5px; font-weight: 600;
  }
  .icon-box {
    display: inline-flex; align-items: center; justify-content: center;
    width: 18px; height: 18px; background: var(--card-black);
  }

  /* Back */
  .card--back {
    background: var(--card-black);
    display: flex; align-items: center; justify-content: center;
  }
  .card--back .brand { font-size: 24px; gap: 12px; }
  .card--back .brand__dot { width: 16px; height: 16px; }
</style>
</head>
<body>
<main class="canvas">

  <section class="card card--front" aria-label="Business card front">
    <div class="front__band">
      <p class="address">
        <svg width="9" height="12" viewBox="0 0 9 12" aria-hidden="true">
          <path d="M4.5 0A4.5 4.5 0 0 0 0 4.5C0 8 4.5 12 4.5 12S9 8 9 4.5A4.5 4.5 0 0 0 4.5 0Zm0 6.3a1.8 1.8 0 1 1 0-3.6 1.8 1.8 0 0 1 0 3.6Z" fill="#ffffff"/>
        </svg>
        <span>415 Marrow St. Suite 108,<br>Boston, MA 02127</span>
      </p>
      <div class="brand"><span class="brand__dot"></span>Olt Investment</div>
    </div>

    <div class="front__details">
      <p class="contact-row contact-row--name"><span class="tag">CEO</span>TEM HOLLIS</p>
      <p class="contact-row">
        <span class="icon-box">
          <svg width="10" height="10" viewBox="0 0 10 10" aria-hidden="true">
            <path d="M2 .5 3.6 2.6 2.7 3.6a6 6 0 0 0 3.7 3.7l1-.9L9.5 8 8.4 9.4C4.5 9.6.4 5.5.6 1.6Z" fill="#ffffff"/>
          </svg>
        </span>508-xxx-xxxx
      </p>
      <p class="contact-row">
        <span class="icon-box">
          <svg width="10" height="8" viewBox="0 0 10 8" aria-hidden="true">
            <rect x=".5" y=".5" width="9" height="7" fill="none" stroke="#ffffff"/>
            <path d="M.5.5 5 4.5 9.5.5" fill="none" stroke="#ffffff"/>
          </svg>
        </span>tem@oltmail.co
      </p>
    </div>
  </section>

  <section class="card card--back" aria-label="Business card back">
    <div class="brand"><span class="brand__dot"></span>Olt Investment</div>
  </section>

</main>
</body>
</html>
```